Modified Business card

We have developed a new logo for the business, and want thou to tray and incorporate it into the business card design that you have done for us.

I am going to upload the logo files. We like the simple clean look that you have on the card, so if you can keep the look incorporating the logo.

Industry/Entity Type

Business

```html
<!DOCTYPE html>
<html lang="en">
<head>
<meta charset="utf-8">
<title>Harlow Engineering – Business Card</title>
<link rel="stylesheet" href="https://fonts.googleapis.com/css2?family=Oswald:wght@400;600&family=Saira+Condensed:wght@600&display=swap">
<style>
  :root {
    --backdrop: #e8e8e8;
    --card: #000000;
    --accent: #d3202a;
    --paper: #ffffff;
    --label: #111111;
  }
  * { margin: 0; padding: 0; box-sizing: border-box; }
  html, body { width: 1200px; height: 848px; overflow: hidden; background: var(--backdrop); }
  .sheet { position: relative; width: 1200px; height: 848px; font-family: "Oswald", sans-serif; }

  .side-label {
    position: absolute; top: 150px;
    font-family: "Saira Condensed", sans-serif; font-weight: 600;
    font-size: 44px; color: var(--label); letter-spacing: 0.5px;
  }
  .side-label--front { left: 60px; }
  .side-label--back { right: 60px; }

  .card {
    position: absolute; top: 250px; width: 500px; height: 310px;
    background: var(--card); box-shadow: 0 18px 30px rgba(0,0,0,0.25);
    overflow: hidden;
  }
  .card--front { left: 50px; }
  .card--back { left: 650px; }

  .edge-strip { position: absolute; top: 0; right: 0; width: 16px; height: 100%; }
  .edge-strip__white { height: 40%; background: var(--paper); }
  .edge-strip__red { height: 60%; background: var(--accent); }

  .brand {
    position: absolute; left: 50%; top: 50%; transform: translate(-50%, -50%);
    display: flex; align-items: center; gap: 14px;
  }
  .brand__mark { width: 60px; height: 60px; background: var(--accent); }
  .brand__name { font-weight: 600; font-size: 30px; color: var(--paper); letter-spacing: 0.5px; }

  .holder { position: absolute; left: 40px; top: 60px; }
  .holder__name { font-weight: 600; font-size: 64px; line-height: 1; color: var(--paper); letter-spacing: 1px; }
  .holder__name .accent { color: var(--accent); }
  .holder__role { font-size: 18px; color: var(--paper); margin-top: 6px; margin-left: 4px; }
  .holder__role .accent { color: var(--accent); }

  .contacts {
    position: absolute; left: 40px; right: 40px; bottom: 34px;
    display: flex; justify-content: space-between; align-items: flex-end;
  }
  .contact { display: flex; flex-direction: column; align-items: flex-start; gap: 6px; }
  .contact svg { width: 18px; height: 18px; fill: none; stroke: var(--paper); stroke-width: 1.4; }
  .contact__text { font-size: 11px; line-height: 1.4; color: var(--paper); letter-spacing: 0.3px; }
</style>
</head>
<body>
<main class="sheet">
  <h2 class="side-label side-label--front">front side</h2>
  <h2 class="side-label side-label--back">back side</h2>

  <section class="card card--front" aria-label="Card front">
    <div class="brand">
      <span class="brand__mark"></span>
      <span class="brand__name">Harlow Engineering</span>
    </div>
    <div class="edge-strip"><div class="edge-strip__white"></div><div class="edge-strip__red"></div></div>
  </section>

  <section class="card card--back" aria-label="Card back">
    <div class="holder">
      <h1 class="holder__name">Tarvin<span class="accent">da</span></h1>
      <p class="holder__role">Graphic <span class="accent">Designer</span></p>
    </div>
    <div class="contacts">
      <div class="contact">
        <svg viewBox="0 0 18 18"><rect x="2" y="4" width="14" height="10"/><polyline points="2,4 9,10 16,4"/></svg>
        <p class="contact__text">tarvinda.studio@mail.com</p>
      </div>
      <div class="contact">
        <svg viewBox="0 0 18 18"><rect x="5" y="2" width="8" height="14" rx="1"/><line x1="8" y1="13.5" x2="10" y2="13.5"/></svg>
        <p class="contact__text">phone : 0800 555 0142<br>fax : 0800 555 0143</p>
      </div>
      <div class="contact">
        <svg viewBox="0 0 18 18"><polygon points="9,2 16,9 12,9 12,16 6,16 6,9 2,9"/></svg>
        <p class="contact__text">address : 12 Orchard Lane</p>
      </div>
    </div>
    <div class="edge-strip"><div class="edge-strip__white"></div><div class="edge-strip__red"></div></div>
  </section>
</main>
</body>
</html>
```